Lunavera Geist und Atem
Zielgruppe
Kosmetikbehandlungen für Sie und Ihn Medizinische Kosmetik, Ultraschall und Fruchtsäurebehandlungen und Hautschälkuren. Make up Artistic und Fußpflege so wie fernöstliche massagen. Die Bausteine Sind Kosmetikbehandlungen, Fernöstlichemassagen aus Hawaai und Bali so we Live Cotcing, Spirituellelebensberatung mit Kartenlegen.
Aufgabenstellung
Es ist nicht einfach was ich möchte. Schauen SIe sich meine Seite an www.stage.lunavera-beispiel.de
die werbeanzeige soll 13 mal 18 cm sein und es wird im Kräuterbund Oberfeld erscheinen, dort machen Heilpraktiker Lebensberater u.v.m. Werbung. Ich möchte das die Anzeige in den Farben von Lunavera weiß,grau, Orange gestaltet wird. Es soll auf mein Institut aufmerksam machen.
z.B Logo lunavera finden sie auf der webseite
Dann Gesundheit, Schönheit, Prävention und Innere Balance
Das Bild von mir welches Sie auf der Webseite sehen sollte auch mit in die Anzeig,e damit die Leute mich sehen können.
Dann der Text:
Tauchen Sie ein in die balinesische Behandlungsphilosophie von Lunavera Geist und Atem.
Dieser Ort umgeben von fließendem Wasser,naturbelassenen Wäldern und reiner klarer Luft zum Durchatmen, liegt mitten im Erlental bei Tannbrunn. Ein Ort der Harmonie und Tiefenentspannung. Das Institut für professionelle Kosmetikbehandlungen, Fernöstliche Massagen sowie Ganzheitliche Lebensberatung und Kartenlegungen. Lassen Sie die Seele baumeln und bringen Sie Ihre Haut von Innen und Außen wieder zum Strahlen. Schönheit und innere Balance ist meine Berufung und diese bringe ich Ihnen Gerne nähe. Sind sie neugierig geworden? Seinen Sie offen und probieren Sie es aus. Und erleben Sie eine ganz besondere Art der Kosmetikbehandlung die viel Nachhaltigkeit mit sich bringt. Finden Sie Ruhe, kraft und kommen Sie wieder bei sich an. Ich bin gerne in allen Bereichen Proffesionel und einfühlsam für Sie da.
Herzliche Grüße
Entfalten Sie Ihre innere Schönheit und strahlen Sie mit viel Selbstbewusstsein und Lebensfreude.
Unser Angebot:
Beratung:
Kartenlegen mit Live-Coaching sowie
Kurzzeitberatungen und Mediale-Beratung.
Professionelle Kosmetikbehandlungen:
Kosmetikbehandlungen bei Problemhaut.
Fruchtsäurebehandlung und HautschÃ..

```html
<!DOCTYPE html>
<html lang="de">
<head>
<meta charset="utf-8">
<title>Lunavera Geist und Atem – Anzeige</title>
<link href="https://fonts.googleapis.com/css2?family=Hind:wght@400;500;600;700&family=Cedarville+Cursive&display=swap" rel="stylesheet">
<style>
  :root {
    --orange: #e8922a;
    --orange-deep: #dc7a16;
    --orange-light: #f3b04d;
    --text-grey: #4f4f4f;
    --soft-grey: #6b6b6b;
    --paper: #ffffff;
  }
  * { box-sizing: border-box; margin: 0; padding: 0; }
  html, body { width: 875px; height: 1200px; overflow: hidden; background: var(--paper); }
  .ad {
    position: relative; width: 875px; height: 1200px;
    background: var(--paper);
    font-family: "Hind", "Helvetica Neue", Arial, sans-serif;
    color: var(--text-grey);
  }
  .brand-name {
    position: absolute; left: 20px; top: 22px;
    font-size: 84px; line-height: 84px; font-weight: 500;
    color: var(--orange); letter-spacing: -1px;
  }
  .brand-tagline {
    position: absolute; left: 140px; top: 112px; white-space: nowrap;
    font-size: 24px; line-height: 28px; color: var(--soft-grey); font-weight: 400;
  }
  .hero {
    position: absolute; left: 16px; top: 150px; width: 828px; height: 267px;
    background: linear-gradient(100deg, var(--orange-deep) 0%, var(--orange) 45%, var(--orange-light) 100%);
    overflow: hidden;
  }
  .hero-slogan {
    position: absolute; left: 32px; top: 30px; width: 500px;
    font-family: "Cedarville Cursive", cursive;
    font-size: 34px; line-height: 49px; color: #fff; letter-spacing: 1px;
  }
  .hero-image {
    position: absolute; left: 545px; top: 20px; width: 205px; height: 247px;
    border-radius: 46% 46% 8% 8% / 38% 38% 8% 8%;
    background: radial-gradient(ellipse at 50% 35%, #d7c6ae 0%, #b59f84 55%, #9b8468 100%);
    opacity: 0.9;
  }
  .intro {
    position: absolute; left: 34px; top: 442px; width: 510px;
    font-size: 18.5px; line-height: 24px; text-align: justify; hyphens: auto;
  }
  .intro p + p { margin-top: 18px; }
  .offer { position: absolute; left: 562px; top: 428px; width: 240px; }
  .offer-title { font-size: 27px; line-height: 34px; font-weight: 400; color: var(--text-grey); margin-bottom: 6px; }
  .offer-heading {
    font-size: 17px; font-weight: 600; color: var(--orange);
    line-height: 21px; margin: 12px 0 5px;
  }
  .offer-list { list-style: none; }
  .offer-list li {
    position: relative; padding-left: 26px; font-size: 16.5px; line-height: 21px;
    margin-bottom: 5px;
  }
  .offer-list li::before {
    content: ""; position: absolute; left: 6px; top: 7px;
    width: 6px; height: 6px; border-radius: 50%; background: var(--text-grey);
  }
  .portrait-frame {
    position: absolute; left: 50px; top: 924px; width: 164px; height: 200px;
    background: #fff; padding: 7px; transform: rotate(-2deg);
    box-shadow: 0 2px 8px rgba(0,0,0,0.3); z-index: 2;
  }
  .portrait {
    width: 100%; height: 100%;
    background: linear-gradient(160deg, #7fb24d 0%, #cfd9b8 45%, #e9e4dc 100%);
  }
  .greeting {
    position: absolute; left: 278px; top: 950px;
    font-size: 18px; line-height: 24px; color: var(--text-grey);
  }
  .greeting .greeting-ihr { padding-left: 42px; }
  .signature {
    position: absolute; left: 272px; top: 988px;
    font-family: "Cedarville Cursive", cursive;
    font-size: 38px; line-height: 48px; color: #555;
  }
  .footer-band {
    position: absolute; left: 30px; top: 1080px; width: 834px; height: 103px;
    background: linear-gradient(100deg, var(--orange-deep), var(--orange) 60%, var(--orange-light));
    color: #fff; font-weight: 700; z-index: 1;
  }
  .footer-note {
    position: absolute; left: 14px; bottom: 10px; width: 230px;
    font-size: 15px; line-height: 19px;
  }
  .footer-contact {
    position: absolute; right: 18px; top: 16px; text-align: right;
    font-size: 16.5px; line-height: 23px; font-style: normal;
  }
</style>
</head>
<body>
<main class="ad">
  <header class="brand">
    <div class="brand-name">lunavera</div>
    <div class="brand-tagline">Geist &amp; Atem</div>
  </header>

  <section class="hero">
    <p class="hero-slogan">Entfalten Sie Ihre innere Schönheit und strahlen Sie mit viel Selbstbewusstsein und Lebensfreude.</p>
    <div class="hero-image" role="img" aria-label="Foto einer steinernen Buddha-Büste"></div>
  </section>

  <article class="intro">
    <p>Tauchen Sie ein in die balinesische Behandlungsphilosophie von Lunavera Geist und Atem. Dieser Ort umgeben von fließendem Wasser, naturbelassenen Wäldern und reiner klarer Luft zum Durchatmen, liegt mitten im Erlental bei Tannbrunn. Ein Ort der Harmonie und Tiefenentspannung. Das Institut für professionelle Kosmetikbehandlungen, Fernöstliche Massagen sowie Ganzheitliche Lebensberatung und Kartenlegungen.</p>
    <p>Lassen Sie die Seele baumeln und bringen Sie Ihre Haut von Innen und Außen wieder zum Strahlen. Schönheit und innere Balance ist meine Berufung und diese bringe ich Ihnen Gerne nähe. Sind sie neugierig geworden? Seinen Sie offen und probieren Sie es aus. Und erleben Sie eine ganz besondere Art der Kosmetikbehandlung die viel Nachhaltigkeit mit sich bringt.</p>
    <p>Finden Sie Ruhe, kraft und kommen Sie wieder bei sich an. Ich bin gerne in allen Bereichen Proffesionel und einfühlsam für Sie da.</p>
  </article>

  <aside class="offer">
    <h2 class="offer-title">Unser Angebot</h2>
    <h3 class="offer-heading">Beratung</h3>
    <ul class="offer-list">
      <li>Kartenlegen mit Live-Coaching sowie Kurzzeit­beratungen und Mediale-Beratung.</li>
    </ul>
    <h3 class="offer-heading">Professionelle Kosmetik­behandlungen</h3>
    <ul class="offer-list">
      <li>Kosmetikbehandlungen bei Problemhaut.</li>
      <li>Fruchtsäurebehandlung und Hautschälkuren.</li>
      <li>Make up Beratungen und Schminkkurse.</li>
    </ul>
    <h3 class="offer-heading">Körperbehandlungen</h3>
    <ul class="offer-list">
      <li>Hot Stone Massage Körper und Gesicht.</li>
      <li>Bali Energetic Gesicht und Körpermassage.</li>
      <li>Reikibehandlungen und Edelsteinmassagen.</li>
      <li>Fußpflege.</li>
    </ul>
  </aside>

  <figure class="portrait-frame">
    <div class="portrait" role="img" aria-label="Porträtfoto des Inhabers Jonas Werling mit grünem Blatt im Vordergrund"></div>
  </figure>

  <div class="greeting">
    <div>Herzliche Grüße</div>
    <div class="greeting-ihr">Ihr</div>
  </div>
  <div class="signature">Jonas Werling</div>

  <footer class="footer-band">
    <p class="footer-note">Jonas Werling bekannt aus dem TV und Premiumparfümerien.</p>
    <address class="footer-contact">
      Lunavera Geist und Atem | Kosmetikfachinstitut Jonas Werling<br>
      Lindenpfad 8 | 72999 Tannbrunn-Erlenbach<br>
      Tel: 01234 567890 | info@lunavera.de | www.lunavera.de
    </address>
  </footer>
</main>
</body>
</html>
```